New letter head for Air Conditioning business

We need a new professional letter head design to suit our new re-branded air conditioning business. Our new logo is attached

```html
<!DOCTYPE html>
<html lang="en">
<head>
<meta charset="utf-8">
<title>Norvale Air Conditioning &amp; Refrigeration – Letterhead</title>
<link rel="stylesheet" href="https://fonts.googleapis.com/css2?family=Roboto:wght@400;700&display=swap">
<style>
  :root {
    --ink: #1d1d1d;
    --accent-red: #ff4566;
    --accent-green: #66ff5b;
    --paper: #ffffff;
  }
  * { margin: 0; padding: 0; box-sizing: border-box; }
  html, body {
    width: 860px;
    height: 1200px;
    overflow: hidden;
    background: var(--paper);
  }
  .letterhead {
    position: relative;
    width: 860px;
    height: 1200px;
    background: var(--paper);
    font-family: "Roboto", Arial, sans-serif;
    color: var(--ink);
  }
  .brand {
    position: absolute;
    left: 58px;
    top: 104px;
    display: flex;
    align-items: center;
    gap: 12px;
  }
  .brand-square {
    width: 26px;
    height: 26px;
    background: var(--accent-green);
  }
  .brand-name {
    font-size: 36px;
    font-weight: 700;
    letter-spacing: 4px;
    color: var(--ink);
    line-height: 1;
  }
  .divider {
    position: absolute;
    left: 417px;
    top: 64px;
    width: 2px;
    height: 128px;
    background: var(--accent-green);
  }
  .contact {
    position: absolute;
    left: 443px;
    top: 68px;
    list-style: none;
    font-size: 16px;
    line-height: 1;
  }
  .contact-title {
    height: 22px;
    margin-bottom: 10px;
  }
  .contact-item {
    display: flex;
    align-items: center;
    height: 22px;
    margin-bottom: 11px;
  }
  .contact-item:last-child { margin-bottom: 0; }
  .contact-icon {
    width: 19px;
    height: 19px;
    margin-right: 12px;
    flex: none;
  }
  .band-red {
    position: absolute;
    left: 0;
    top: 1107px;
    width: 860px;
    height: 53px;
    background: var(--accent-red);
  }
  .band-green {
    position: absolute;
    left: 0;
    top: 1160px;
    width: 860px;
    height: 40px;
    background: var(--accent-green);
  }
</style>
</head>
<body>
<main class="letterhead">
  <header>
    <div class="brand">
      <span class="brand-square"></span>
      <span class="brand-name">NORVALE</span>
    </div>
    <div class="divider"></div>
    <ul class="contact">
      <li class="contact-title">Norvale Air Conditioning &amp; Refrigeration Address</li>
      <li class="contact-item">
        <svg class="contact-icon" viewBox="0 0 24 24" aria-hidden="true">
          <path fill="var(--accent-red)" d="M6.6 2.2c.7-.4 1.5-.1 1.9.6l1.6 3c.3.6.2 1.3-.3 1.8L8.5 8.9c1.2 2.6 3.4 4.8 6 6l1.3-1.3c.5-.5 1.2-.6 1.8-.3l3 1.6c.7.4 1 1.2.6 1.9l-.9 1.8c-.6 1.2-2 1.8-3.3 1.4C10.5 18 5.9 13.4 4 7.1c-.4-1.3.2-2.7 1.4-3.3z"/>
        </svg>
        <span>+60 5550 4821</span>
      </li>
      <li class="contact-item">
        <svg class="contact-icon" viewBox="0 0 24 24" aria-hidden="true">
          <g fill="none" stroke="var(--accent-red)" stroke-width="1.8">
            <rect x="2" y="5" width="20" height="14"/>
            <path d="M2 5l10 8 10-8M2 19l7.5-7M22 19l-7.5-7"/>
          </g>
        </svg>
        <span>info@norvaleairconditionandrefrigeration.com</span>
      </li>
      <li class="contact-item">
        <svg class="contact-icon" viewBox="0 0 24 24" aria-hidden="true">
          <g fill="none" stroke="var(--accent-red)" stroke-width="1.6">
            <circle cx="12" cy="12" r="10"/>
            <ellipse cx="12" cy="12" rx="4.5" ry="10"/>
            <path d="M2 12h20M4 7h16M4 17h16M12 2v20"/>
          </g>
        </svg>
        <span>www.norvaleairconditionandrefrigeration.com</span>
      </li>
    </ul>
  </header>
  <footer>
    <div class="band-red"></div>
    <div class="band-green"></div>
  </footer>
</main>
</body>
</html>
```